BRIGHT LEDGER NOW

I'm virtually ready to launch my site, but I have a number of edits and modifications that need to be implemented. More importantly, I'm always looking to improve my site, particularly now that I am making my proverbial "FIRST IMPRESSION." Thus, I'm willing to see if there is someone who can add creativity and perhaps improve what I already have, particularly on the All Important Front Page.

Need extra days to review

```html
<!DOCTYPE html>
<html lang="en">
<head>
<meta charset="utf-8">
<title>Bright Ledger Now</title>
<link href="https://fonts.googleapis.com/css2?family=Poppins:wght@300;400;500;600;700;800&display=swap" rel="stylesheet">
<style>
:root{
  --navy:#0b2350;
  --red:#b00714;
  --gray-bg:#eeeeee;
  --text:#6b6b6b;
  --dark:#1d1d1d;
  --black:#000000;
  --white:#ffffff;
}
*{box-sizing:border-box;margin:0;padding:0}
html,body{width:1200px;height:3159px;overflow:hidden;background:var(--white)}
body{font-family:'Poppins',sans-serif;position:relative;color:var(--dark)}
.abs{position:absolute}
.pill{position:absolute;border-radius:22px;font-size:15px;font-weight:500;display:flex;align-items:center;justify-content:center;text-transform:uppercase}
.pill-red{background:var(--red);color:var(--white)}
.pill-white{background:var(--white);color:var(--navy)}

/* header */
.topbar{left:0;top:0;width:1200px;height:95px;background:var(--white)}
.brand{left:95px;top:-2px;width:164px;height:164px;border-radius:50%;background:var(--white);box-shadow:0 2px 8px rgba(0,0,0,.12);z-index:3;display:flex;align-items:center;justify-content:center;text-align:center}
.brand span{font-size:17px;font-weight:800;color:var(--navy);line-height:1.15;width:110px}
.contact-icon{width:46px;height:46px;border-radius:50%;border:1px solid #d9d9d9;display:flex;align-items:center;justify-content:center}
.contact-label{font-size:11px;color:#444}
.contact-value{font-size:14px;color:var(--dark);line-height:1.8}
.navbar{left:0;top:95px;width:1200px;height:46px;background:var(--red)}
.navbar a{position:absolute;top:15px;font-size:13px;font-weight:500;color:var(--white);text-decoration:none}

/* hero */
.hero{left:0;top:141px;width:1200px;height:510px;background:
  radial-gradient(ellipse 160px 220px at 600px 250px,rgba(40,45,60,.55),transparent 70%),
  radial-gradient(ellipse 140px 200px at 330px 330px,rgba(35,45,70,.5),transparent 70%),
  radial-gradient(ellipse 140px 200px at 820px 330px,rgba(60,60,70,.45),transparent 70%),
  linear-gradient(180deg,#9aa6b8 0%,#5d6b86 45%,#263654 100%)}
.hero-title{left:0;top:393px;width:1200px;text-align:center;font-size:50px;font-weight:800;color:var(--white)}
.hero-sub{left:0;top:469px;width:1200px;text-align:center;font-size:17px;font-weight:700;color:var(--white)}

/* about */
.about-photo{left:104px;top:772px;width:436px;height:436px;border-radius:50%;border:8px solid var(--navy);background:
  radial-gradient(circle at 80% 30%,rgba(60,140,90,.7) 0 40px,transparent 41px),
  radial-gradient(circle at 75% 75%,rgba(230,150,50,.7) 0 55px,transparent 60px),
  linear-gradient(135deg,#cfcbbd 0%,#a5a08c 50%,#d9c89a 100%)}
.section-title{font-size:38px;font-weight:800;color:var(--navy)}
.about-text{left:603px;width:485px;font-size:17px;line-height:30px;color:var(--text);text-align:justify;font-weight:300}

/* services */
.services{left:0;top:1306px;width:1200px;height:834px;background:var(--gray-bg)}
.card{width:310px;height:363px;top:1647px;background:var(--white);border-radius:22px;box-shadow:0 2px 8px rgba(0,0,0,.06)}
.card-photo{width:186px;height:186px;border-radius:50%;border-bottom:6px solid var(--red);top:1607px}
.card-title{width:310px;text-align:center;font-size:17px;font-weight:500;color:#222;line-height:25px}
.card-text{width:310px;text-align:center;font-size:17px;line-height:30px;color:var(--text);font-weight:300;padding:0 22px;max-height:90px;overflow:hidden}
.arrow{width:30px;height:30px;border:1.5px solid var(--navy);border-radius:50%;display:flex;align-items:center;justify-content:center}

/* faq */
.faq-photo{left:740px;top:2142px;width:460px;height:708px;background:
  radial-gradient(ellipse 90px 120px at 270px 140px,rgba(190,150,120,.55),transparent 70%),
  linear-gradient(90deg,#ffffff 0%,rgba(225,215,205,.7) 22%,#6d7b97 50%,#2c3c62 78%,#24345a 100%)}
.faq-item{left:111px;width:665px;height:60px;background:var(--white);box-shadow:0 1px 6px rgba(0,0,0,.08);display:flex;align-items:center;padding:0 52px 0 30px;font-size:16px;color:#111;line-height:23px}
.faq-item::after{content:"+";position:absolute;right:30px;top:17px;font-size:20px;color:#999}

/* footer */
.footer{left:0;top:2850px;width:1200px;height:309px;background:var(--black)}
.foot-head{font-size:14px;font-weight:600;color:var(--red)}
.foot-link{font-size:13px;color:#cfcfcf}
.foot-contact{font-size:13px;font-weight:500;color:var(--white)}
.divider{width:1px;background:#444}
</style>
</head>
<body>

<div class="abs topbar"></div>
<div class="abs brand"><span>BRIGHT LEDGER NOW</span></div>

<div class="abs contact-icon" style="left:270px;top:24px">
  <svg width="22" height="22" viewBox="0 0 24 24"><path fill="#0b2350" d="M6.6 10.8a15 15 0 0 0 6.6 6.6l2.2-2.2c.3-.3.7-.4 1-.2 1.1.4 2.300.6 3.600.6.600 0 1 .4 1 1V20c0 .6-.4 1-1 1A17 17 0 0 1 3 4c0-.6.4-1 1-1h3.5c.6 0 1 .4 1 1 0 1.3.2 2.5.6 3.6.1.3 0 .7-.2 1z"/></svg>
</div>
<div class="abs contact-label" style="left:333px;top:27px">Call US</div>
<div class="abs contact-value" style="left:333px;top:45px">602.555.0148 / 800.555.0172</div>

<div class="abs contact-icon" style="left:543px;top:24px">
  <svg width="24" height="24" viewBox="0 0 24 24"><circle cx="12" cy="12" r="10" fill="#0b2350"/><path fill="#fff" d="M8 6c2 1 3 2 2 4s-3 1-3 3 2 2 2 4c-2-1-4-3-4-5s1-5 3-6zm7 2c2 0 3 2 3 4s-1 3-2 4c0-2-2-2-2-4s1-2 1-4z"/></svg>
</div>
<div class="abs contact-label" style="left:603px;top:27px">Send Us Website</div>
<div class="abs contact-value" style="left:603px;top:45px">WWW.BRIGHTLEDGERNOW.COM</div>

<div class="abs contact-icon" style="left:833px;top:24px">
  <svg width="20" height="22" viewBox="0 0 24 24"><path fill="#0b2350" d="M12 2a7 7 0 0 0-7 7c0 5 7 13 7 13s7-8 7-13a7 7 0 0 0-7-7zm0 9.5A2.5 2.5 0 1 1 12 6.5a2.5 2.5 0 0 1 0 5z"/></svg>
</div>
<div class="abs contact-label" style="left:893px;top:14px">LOCATION</div>
<div class="abs contact-value" style="left:893px;top:32px;line-height:26px">4820 West Harbor Ave., Suite<br>210 Mesa, Arizona 85201</div>

<nav class="abs navbar">
  <a style="left:269px">HOME</a>
  <a style="left:365px">ABOUT</a>
  <a style="left:461px">CONTCAT</a>
  <a style="left:584px">PRODUCT</a>
  <a style="left:711px">OVERVIEW</a>
  <a style="left:842px">WATCH DEMO</a>
  <a style="left:1024px">FEATURES</a>
</nav>

<div class="abs hero" role="img" aria-label="Team of five business professionals in suits standing in a bright office"></div>
<h1 class="abs hero-title">WELCOME TO BRIGHT LEDGER NOW</h1>
<p class="abs hero-sub">Contact us to find out how you can join us to BRIGHT LEDGER NOW!!</p>
<div class="pill pill-white" style="left:389px;top:525px;width:131px;height:40px">Learn More</div>
<div class="pill pill-red" style="left:534px;top:525px;width:277px;height:40px">Schedule Free&nbsp; Consultation</div>

<div class="abs about-photo" role="img" aria-label="Close-up of a hundred dollar bill with the portrait wearing a face mask"></div>
<h2 class="abs section-title" style="left:603px;top:760px">ABOUT US</h2>
<p class="abs about-text" style="top:843px">BLN is a group of attorney and legal assistants with many years of experience in litigation, who are devoted to PREVENTING LEGAL CLAIMS and COSTLY LAWSUITS through a variety of FREE and VERY AFFORDABLE services described below.</p>
<p class="abs about-text" style="top:1022px">OUR UNIQUE SERVICE PLAN MAKES IT POSSIBLE FOR US TO BRIGHT LEDGER NOW.</p>
<div class="pill pill-red" style="left:603px;top:1126px;width:131px;height:40px">Read More</div>

<div class="abs services"></div>
<h2 class="abs section-title" style="left:0;top:1402px;width:1200px;text-align:center">OUR SERVICES</h2>
<p class="abs" style="left:200px;top:1485px;width:800px;text-align:center;font-size:17px;line-height:30px;color:var(--text);font-weight:300">The price for a membership is a ridiculously low $9.95 PER WEEK. We believe that this fee is very affordable. So what is it? Membership includes the following:</p>

<div class="abs arrow" style="left:42px;top:1834px"><svg width="12" height="12" viewBox="0 0 12 12"><path d="M8 1 3 6l5 5" fill="none" stroke="#0b2350" stroke-width="1.5"/></svg></div>
<div class="abs arrow" style="left:1127px;top:1833px"><svg width="12" height="12" viewBox="0 0 12 12"><path d="m4 1 5 5-5 5" fill="none" stroke="#0b2350" stroke-width="1.5"/></svg></div>

<div class="abs card" style="left:111px"></div>
<div class="abs card-photo" style="left:173px;background:radial-gradient(ellipse 45px 80px at 45% 65%,#2e2a2a,transparent 75%),linear-gradient(135deg,#ecebe8,#b9b6b2 60%,#7f7b78)" role="img" aria-label="Smiling woman in a blazer with arms crossed in an office"></div>
<div class="abs card-title" style="left:111px;top:1824px">FREE INITIAL CONSULTATION</div>
<div class="abs card-text" style="left:111px;top:1867px">As a prospective Bright Ledger Now (“BLN”) member, we urge you to schedule</div>
<div class="pill pill-red" style="left:201px;top:1981px;width:131px;height:40px">Learn More</div>

<div class="abs card" style="left:446px"></div>
<div class="abs card-photo" style="left:508px;background:radial-gradient(ellipse 60px 50px at 40% 75%,#1d2230,transparent 75%),linear-gradient(135deg,#c8b990,#9a8c72 45%,#3a3d46)" role="img" aria-label="Businesswoman presenting a folder to a client across a desk"></div>
<div class="abs card-title" style="left:446px;top:1809px">PROPRIETARY<br>CONTRACT LANGUAGE</div>
<div class="abs card-text" style="left:446px;top:1865px">BLN members are entitled to incorporate exclusive proprietary contract</div>
<div class="pill pill-red" style="left:535px;top:1981px;width:131px;height:40px">Learn More</div>

<div class="abs card" style="left:777px"></div>
<div class="abs card-photo" style="left:839px;background:linear-gradient(90deg,#5b5858 0%,#7a7676 40%,#e6e6e6 60%,#f4f4f4 100%)" role="img" aria-label="Attorney in white blouse taking notes while meeting a client"></div>
<div class="abs card-title" style="left:777px;top:1820px">FREE CONSULTATION</div>
<div class="abs card-text" style="left:777px;top:1867px">BLN members can call their local BLN Attorney any time, and be given</div>
<div class="pill pill-red" style="left:866px;top:1981px;width:131px;height:40px">Learn More</div>

<div class="abs faq-photo" role="img" aria-label="Confident businessman in a navy suit with arms crossed"></div>
<h2 class="abs section-title" style="left:0;top:2220px;width:1197px;text-align:center;font-size:40px">FREQUENTLY ASKED QUESTIONS</h2>
<div class="abs faq-item" style="top:2349px">Why should I be concerned about legal claims?</div>
<div class="abs faq-item" style="top:2430px">Provide more details about the value of BLN’s contract language.</div>
<div class="abs faq-item" style="top:2510px">If I’m a contractor, for example, how can an BLN membership minimize legal claims against my business?</div>
<div class="abs faq-item" style="top:2591px">What does an BLN membership cost?</div>
<div class="abs faq-item" style="top:2671px">Do you have a Referral Program?</div>

<footer class="abs footer"></footer>
<div class="abs foot-head" style="left:113px;top:2924px">QUICK LINKS</div>
<div class="abs foot-link" style="left:113px;top:2966px;line-height:24px">HOME<br>ABOUT<br>SERVICES<br>FAQ</div>
<div class="abs foot-link" style="left:225px;top:2966px;line-height:24px">CONTACT US<br>TERMS OF SERVICE<br>PRIVACY POLICY</div>
<div class="abs divider" style="left:392px;top:2928px;height:182px"></div>
<div class="abs foot-head" style="left:418px;top:2924px">SOCIAL MEDIA</div>
<svg class="abs" style="left:413px;top:2959px" width="112" height="28" viewBox="0 0 112 28"><circle cx="14" cy="14" r="13" fill="#3a3a3a"/><circle cx="56" cy="14" r="13" fill="#3a3a3a"/><circle cx="98" cy="14" r="13" fill="#3a3a3a"/></svg>
<div class="abs divider" style="left:580px;top:2928px;height:182px"></div>
<div class="abs foot-head" style="left:645px;top:2924px">CONTACT</div>
<svg class="abs" style="left:645px;top:2962px" width="14" height="16" viewBox="0 0 24 24"><path fill="#fff" d="M12 2a7 7 0 0 0-7 7c0 5 7 13 7 13s7-8 7-13a7 7 0 0 0-7-7zm0 9.5A2.5 2.5 0 1 1 12 6.5a2.5 2.5 0 0 1 0 5z"/></svg>
<div class="abs foot-contact" style="left:682px;top:2962px">4820 WEST HARBOR AVE., SUITE 210, MESA, ARIZONA 85201</div>
<svg class="abs" style="left:645px;top:3002px" width="15" height="15" viewBox="0 0 24 24"><path fill="#fff" d="M6.6 10.8a15 15 0 0 0 6.6 6.6l2.2-2.2c.3-.3.7-.4 1-.2 1.1.4 2.3.6 3.6.6.6 0 1 .4 1 1V20c0 .6-.4 1-1 1A17 17 0 0 1 3 4c0-.6.4-1 1-1h3.5c.6 0 1 .4 1 1 0 1.3.2 2.5.6 3.6.1.3 0 .7-.2 1z"/></svg>
<div class="abs foot-contact" style="left:678px;top:3001px">(602) 555-0193 / (800) 555-0126</div>
<svg class="abs" style="left:644px;top:3037px" width="16" height="16" viewBox="0 0 24 24"><circle cx="12" cy="12" r="10" fill="#fff"/><path fill="#000" d="M8 6c2 1 3 2 2 4s-3 1-3 3 2 2 2 4c-2-1-4-3-4-5s1-5 3-6zm7 2c2 0 3 2 3 4s-1 3-2 4c0-2-2-2-2-4s1-2 1-4z"/></svg>
<div class="abs foot-contact" style="left:678px;top:3036px">WWW.BRIGHTLEDGERNOW.COM</div>
<div class="abs" style="left:111px;top:3110px;width:980px;height:1px;background:#333"></div>
<div class="abs" style="left:113px;top:3119px;font-size:12px;color:#bdbdbd">Copyright© 2023 BRIGHTLEDGERNOW.NET | All Rights Reserved</div>

</body>
</html>
```